packaging Design Project

We would like to receive amazing design for our packaging sanitary napkin brand VELORA to catch customers
1)we have attached a file named CORALIE design but it is just a reference for taking the information please avoid to do a similar design as the brands are differents .As reference for the map of the design some modifications should be done on the sizes as per the following:
instead 12mm/24mm/90mm/24mm/12mm
it should be 25mm/35mm/120mm/35mm/25mm
instead 83mm/48mm/83mm/48mm/
it should be 105mm/65mm/105mm/65mm
2)our contact information have been changed and the new ones are as per the following:
Phone:(509)3-628-4175
:(509)3-742-1938
E-mail:info@harborvaleco.example
3)we have attached the VELORA sanitary pictures to be redesigned as per Lunette is done on its packaging.This is a very important point of the the design you will submit.
4)our company logo is attached
5)we need the design in CMYK format as it is for printing with the specified pantone number .
6)you can pick pictures from pixquarry.example if you win we will buy it.
7)Please go to the supermarket or drugstore to have a better idea how the design should be but we are not required a copy of any brand.
8)five water drops in red or pink color should be in the both front to indicate the high absorption quality.
9) 8 pads.serviettes.toallas to indicate the qty per package.
10)a big word (MAXI) should be writted in the both front to indicate its high absorption.
11)275mm to indicate the lenght.
12)write SANITARY NAPKIN below the word VELORA.
13)reduce the size of our company logo and put it in the both front at the top on the left side.
14)please read the brief time to time because we are upgraded information time to time too.
15)Any doubt or question please send me a message.
N.B: the packaging design should be able to compete with LUNETTE MAXI or Dovira so be creative to develop an amazing and innovative design.
Updates
please redesign the velora sanitary picture with each detail to be attractive,this is one of most importamt part of the design.
Reason: need more designs and some designers have required more time.
now the deadline is for may 13th.
please do not put barcode number.
Reason: need of amazing designs
don't work with the coralie sanitary picture but with the velora sanitary picture.you should design the velora sanitary picture to refelct all of its details to be amazing.
Reason: lack of good designs
Target Market(s)
woman from 12 to 45 years old
Industry/Entity Type
It Company
Requirements
Must have
- A)the design should have two fronts and the same information in the both front.
B) (MAXI) should be writted in the both front to indicate its high capacity of absorption.
C)five blood drops in red or pink color should be in the both front to indicate the high absorption quality.
D) 8 pads.serviettes.toallas to indicate the qty per package.
E)275mm to indicate the lenght
F)write SANITARY NAPKIN below the word
G)use fresh and innovative colors but feminine colors .
Nice to have
-reduce the size of our company logo and put it in the both front at the top of the left side.
Should not have
- -please don't put flowers because the pad dosen't have any scent or perfume.
-Please do not put barcode number.

```html
<!DOCTYPE html>
<html lang="en">
<head>
<meta charset="utf-8">
<title>Velora Maxi – Sanitary Napkin Pack Front</title>
<link rel="stylesheet" href="https://fonts.googleapis.com/css2?family=Great+Vibes&family=Playfair+Display:wght@400;700&family=Arimo:wght@400;700&display=swap">
<style>
  :root {
    --blush: #f6e3f3;
    --lilac-light: #e6c9ea;
    --lilac: #cfa6dc;
    --lilac-deep: #b384c6;
    --violet: #7c5a9e;
    --lace: #3c3a3e;
    --lace-edge: #e9c6e4;
    --ink: #1b1b1b;
    --white: #ffffff;
    --pad-light: #f3f7fd;
    --pad-blue: #c9d9f2;
    --drop-pink: #e0457b;
  }
  * { margin: 0; padding: 0; box-sizing: border-box; }
  html, body { width: 1200px; height: 1004px; overflow: hidden; background: var(--white); }
  .pack-front {
    position: relative;
    width: 1200px;
    height: 1004px;
    overflow: hidden;
    background: var(--blush);
  }
  .pack-background { position: absolute; inset: 0; }
  .lace-band { position: absolute; left: 0; width: 1200px; }
  .lace-band--top {
    top: 0;
    height: 162px;
    background: linear-gradient(to bottom, var(--lace) 0%, var(--lace) 72%, var(--lace-edge) 72%, var(--lilac-light) 100%);
  }
  .lace-band--bottom {
    bottom: 0;
    height: 228px;
    background: linear-gradient(to top, var(--lace) 0%, var(--lace) 74%, var(--lace-edge) 74%, var(--lilac-light) 100%);
  }
  .brand-name {
    position: absolute;
    left: 170px;
    top: 160px;
    font-family: "Great Vibes", cursive;
    font-size: 260px;
    line-height: 1;
    color: var(--ink);
    font-weight: 400;
  }
  .variant-name {
    position: absolute;
    left: 596px;
    top: 402px;
    font-family: "Playfair Display", serif;
    font-size: 104px;
    line-height: 1;
    color: var(--ink);
    letter-spacing: -2px;
  }
  .pad-visual {
    position: absolute;
    left: 62px;
    top: 470px;
    width: 112px;
    height: 236px;
    border-radius: 56px;
    background: linear-gradient(160deg, var(--pad-light) 0%, var(--pad-blue) 100%);
    box-shadow: 14px 16px 0 rgba(179, 132, 198, 0.45);
    transform: rotate(-14deg);
  }
  .length-marker {
    position: absolute;
    left: 176px;
    top: 464px;
    width: 200px;
    height: 230px;
  }
  .length-label {
    position: absolute;
    left: 248px;
    top: 566px;
    font-family: "Playfair Display", serif;
    font-weight: 700;
    font-size: 30px;
    color: var(--ink);
  }
  .length-label small { font-size: 20px; font-weight: 400; }
  .stripe-wave {
    position: absolute;
    left: 448px;
    top: 462px;
    width: 752px;
    height: 240px;
  }
  .absorbency-drops {
    position: absolute;
    left: 992px;
    top: 674px;
    width: 108px;
    height: 30px;
  }
  .pack-info {
    position: absolute;
    left: 440px;
    top: 728px;
    font-family: "Arimo", sans-serif;
    font-size: 35px;
    line-height: 1;
    color: var(--ink);
    white-space: nowrap;
  }
  .pack-info__type { color: var(--white); margin-right: 10px; }
  .pack-info__count { font-weight: 700; font-size: 40px; }
</style>
</head>
<body>
<main class="pack-front">
  <svg class="pack-background" width="1200" height="1004" viewBox="0 0 1200 1004" aria-hidden="true">
    <defs>
      <linearGradient id="band-lilac" x1="0" y1="0" x2="1" y2="0">
        <stop offset="0" stop-color="#e2c2e8"/>
        <stop offset="1" stop-color="#c99ad8"/>
      </linearGradient>
    </defs>
    <rect width="1200" height="1004" fill="#f3dcf1"/>
    <path d="M0 150 H1200 V250 C1000 300 800 230 600 250 C400 270 200 230 0 260 Z" fill="url(#band-lilac)"/>
    <path d="M0 300 C250 250 500 330 760 300 C960 280 1100 300 1200 320 V360 C1000 340 800 360 560 380 C340 400 160 360 0 380 Z" fill="#e8cdef" opacity="0.8"/>
    <path d="M0 520 C200 560 350 600 480 640 L480 760 C300 740 150 700 0 680 Z" fill="#d6b1e0" opacity="0.7"/>
    <path d="M0 700 C300 740 700 770 1200 720 V800 H0 Z" fill="#d9b6e3"/>
    <path d="M0 740 C300 780 700 790 1200 760 V800 H0 Z" fill="#c9a0d8" opacity="0.6"/>
  </svg>

  <div class="lace-band lace-band--top" role="img" aria-label="Dark lace trim border with rose motifs"></div>
  <div class="lace-band lace-band--bottom" role="img" aria-label="Dark lace trim border with rose motifs"></div>

  <h1 class="brand-name">Velora</h1>
  <p class="variant-name">MAXI</p>

  <svg class="stripe-wave" viewBox="0 0 752 240" role="img" aria-label="Flowing ribbon of dark and violet stripes">
    <defs>
      <linearGradient id="stripe-fill" x1="0" y1="0" x2="1" y2="0">
        <stop offset="0" stop-color="#9c7bb8"/>
        <stop offset="0.5" stop-color="#6f4f8e"/>
        <stop offset="1" stop-color="#3a2b48"/>
      </linearGradient>
    </defs>
    <path d="M0 160 C120 120 220 60 360 40 C500 20 640 30 752 12 V226 C620 206 480 200 340 214 C200 228 100 238 0 236 Z" fill="url(#stripe-fill)"/>
  </svg>

  <div class="pad-visual" role="img" aria-label="Illustration of a white winged sanitary pad with blue absorbent core"></div>

  <svg class="length-marker" viewBox="0 0 200 230" aria-hidden="true">
    <defs>
      <marker id="arrow-head" viewBox="0 0 10 10" refX="8" refY="5" markerWidth="7" markerHeight="7" orient="auto-start-reverse">
        <path d="M0 0 L10 5 L0 10 Z" fill="#1b1b1b"/>
      </marker>
    </defs>
    <path d="M14 14 C40 110 100 190 186 212" fill="none" stroke="#1b1b1b" stroke-width="3" marker-start="url(#arrow-head)" marker-end="url(#arrow-head)"/>
  </svg>
  <p class="length-label">275 <small>mm</small></p>

  <svg class="absorbency-drops" viewBox="0 0 108 30" role="img" aria-label="Absorbency level: five drops">
    <g fill="#e0457b">
      <path d="M10 2 C14 10 18 15 18 20 A8 8 0 0 1 2 20 C2 15 6 10 10 2 Z"/>
      <path d="M32 2 C36 10 40 15 40 20 A8 8 0 0 1 24 20 C24 15 28 10 32 2 Z"/>
      <path d="M54 2 C58 10 62 15 62 20 A8 8 0 0 1 46 20 C46 15 50 10 54 2 Z"/>
      <path d="M76 2 C80 10 84 15 84 20 A8 8 0 0 1 68 20 C68 15 72 10 76 2 Z"/>
      <path d="M98 2 C102 10 106 15 106 20 A8 8 0 0 1 90 20 C90 15 94 10 98 2 Z"/>
    </g>
  </svg>

  <p class="pack-info">
    <span class="pack-info__type">sanitary napkin</span>
    <span class="pack-info__count">8</span> pads servittes toallas
  </p>
</main>
</body>
</html>
```